Quorvel Landing page redesign

We are looking for a landing page redesign before we officially launch. We want to incorporate the information already on the site at www.Quorvel-example.com landing page but make it more inviting. There needs to be a sign up section along with clearly stating what we do. Having a place for sample profiles and linking to our blog and podcast is option. More information about all we will be doing is at Quorvel is on the landing page and also on the blog.

Target Market(s)

35 years old and up.

Coding

Coded - Design and coding required

Number of Pages Required

1 page

Requirements
Must have
• The top bar and the bottom bar (with the privacy policy, etc)
• Sign in/up section.
• I don't want to give to much here because I want designers to be creative.
Nice to have
• Prefer not to have a landing page that requires a lot of scrolling at all.

```html
<!DOCTYPE html>
<html lang="en">
<head>
<meta charset="utf-8">
<title>Quorvel</title>
<link href="https://fonts.googleapis.com/css2?family=Roboto:wght@300;400;500;700&display=swap" rel="stylesheet">
<style>
:root{
  --navy:#141b5c;
  --ink:#222;
  --muted:#666;
  --soft:#999;
  --line:#e4e4e4;
  --panel:#e6e6e6;
  --white:#fff;
}
*{box-sizing:border-box;margin:0;padding:0}
html,body{width:962px;height:1200px;overflow:hidden}
body{position:relative;font-family:'Roboto',Arial,sans-serif;color:var(--ink);background:var(--white)}
a{text-decoration:none;color:inherit}
.abs{position:absolute}

/* header */
.site-header{top:0;left:0;width:962px;height:54px;border-bottom:1px solid var(--line)}
.brand{display:flex;align-items:center}
.brand-name{font-size:16px;font-weight:400;letter-spacing:.3px}
.site-header .brand{position:absolute;left:72px;top:17px;color:var(--navy)}
.login-btn{left:797px;top:10px;width:59px;height:33px;border:1px solid var(--navy);font-size:8.5px;font-weight:500;color:var(--navy);display:flex;align-items:center;justify-content:center;letter-spacing:.3px}
.menu-toggle{left:876px;top:22px;width:15px}
.menu-toggle span{display:block;height:1.6px;background:var(--ink);margin-bottom:3px}

/* hero */
.hero-title{left:71px;top:158px;font-size:29px;font-weight:300;color:var(--ink)}
.rule{height:1px;width:32px;background:#ccc}
.hero-rule{left:71px;top:200px}
.hero-copy{left:71px;top:213px;width:284px;font-size:10.5px;line-height:18px;color:#555}
.btn{height:32px;display:flex;align-items:center;justify-content:center;font-size:8.5px;font-weight:500;letter-spacing:.2px}
.btn-solid{left:71px;top:264px;width:149px;background:var(--navy);color:#fff}
.btn-outline{left:228px;top:264px;width:149px;border:1px solid var(--navy);color:var(--navy)}
.hero-visual{left:448px;top:108px;width:438px;height:232px;border-radius:8px;background:linear-gradient(180deg,#f1f1f1,#dcdcdc)}

/* get started band */
.band{left:0;top:413px;width:962px;height:297px;background:var(--navy)}
.signup-card{left:71px;top:477px;width:281px;height:233px;background:#fff;box-shadow:0 -8px 24px rgba(0,0,0,.3);padding:0 31px}
.signup-title{margin-top:39px;font-size:17.5px;font-weight:400;color:var(--ink)}
.field-label{margin-top:15px;font-size:10.5px;color:var(--muted);display:flex;align-items:center;gap:5px}
.field-input{margin-top:7px;height:32px;border:1px solid var(--line);font-size:9px;color:var(--soft);padding:11px 12px}
.subscribe-btn{margin-top:10px;height:32px;border:2px solid var(--navy);font-size:8.5px;font-weight:500;color:var(--navy);display:flex;align-items:center;justify-content:center}
.signin-note{margin-top:15px;font-size:10.5px;color:var(--muted)}
.signin-note a{color:var(--navy);text-decoration:underline}

.started-title{left:424px;top:464px;font-size:21px;font-weight:300;color:#fff}
.started-rule{left:424px;top:498px;background:rgba(255,255,255,.35)}
.feature{display:flex;gap:18px;color:#fff;font-size:10.5px;line-height:19px}
.feature b{font-size:12px;font-weight:700}
.feature svg{flex:none;width:24px;height:24px;margin-top:-2px}

/* blog */
.blogs-title{left:0;width:962px;top:762px;text-align:center;font-size:21px;font-weight:300}
.blogs-rule{left:465px;top:798px}
.post{top:826px;width:262px}
.post-media{position:relative;height:142px}
.post-media .img{position:absolute;left:0;top:0;width:262px;height:119px}
.post-media .tab{position:absolute;right:0;top:119px;width:19px;height:23px}
.logo-panel .img,.logo-panel .tab{background:var(--panel)}
.logo-panel .podcast-name{position:absolute;left:0;top:40px;width:262px;text-align:center;font-size:25px;font-weight:500;color:var(--navy);letter-spacing:.3px}
.photo-panel .img{background:linear-gradient(135deg,#6d5a3e,#b98e5c 45%,#3d3326)}
.photo-panel .tab{background:#3d3326}
.post-cat{margin-top:2px;font-size:8.5px;font-weight:500;color:var(--soft);letter-spacing:.2px}
.post-title{margin-top:3px;font-size:13px;font-weight:400;color:var(--ink)}
.post .rule{width:18px;margin-top:7px;background:#ddd}
.post-excerpt{margin-top:9px;width:218px;font-size:9.5px;line-height:18px;color:var(--muted)}

/* footer */
.site-footer{left:0;top:1099px;width:962px;height:101px;background:var(--navy);color:#fff}
.site-footer .brand{position:absolute;left:72px;top:21px}
.footer-nav{position:absolute;left:331px;top:26px;display:flex;gap:24px;font-size:11px}
.social{position:absolute;left:830px;top:27px;display:flex;gap:10px;font-size:9px}
.footer-line{position:absolute;left:71px;top:59px;width:820px;height:1px;background:rgba(255,255,255,.15)}
.copyright{position:absolute;left:0;width:962px;top:75px;text-align:center;font-size:9.5px}
</style>
</head>
<body>

<header class="abs site-header">
  <div class="brand"><span class="brand-name">Quorvel</span></div>
  <a class="abs login-btn">LOGIN</a>
  <div class="abs menu-toggle"><span></span><span></span><span></span></div>
</header>

<section class="hero">
  <h1 class="abs hero-title">Welcome to Quorvel</h1>
  <div class="abs rule hero-rule"></div>
  <p class="abs hero-copy">Build multiple Quorvel pages through one account for yourself, your family and to keep loved one's legacies alive.</p>
  <a class="abs btn btn-solid">SAMPLE QUORVEL PROFILE</a>
  <a class="abs btn btn-outline">SAMPLE LEGACY PROFILE</a>
  <div class="abs hero-visual" role="img" aria-label="Laptop showing a Family and Friends connections screen"></div>
</section>

<section class="abs band"></section>

<div class="abs signup-card">
  <h2 class="signup-title">Become an early user</h2>
  <div class="field-label">
    <svg width="9" height="7" viewBox="0 0 9 7"><rect x=".5" y=".5" width="8" height="6" fill="none" stroke="#aaa"/><path d="M.5 .5 4.5 4 8.5 .5" fill="none" stroke="#aaa"/></svg>
    Email
  </div>
  <div class="field-input">Enter email address...</div>
  <div class="subscribe-btn">SUBSCRIBE</div>
  <p class="signin-note">Already have an account? <a>Sign in</a></p>
</div>

<h2 class="abs started-title">Get started with Quorvel</h2>
<div class="abs rule started-rule"></div>

<div class="abs feature" style="left:424px;top:525px;width:190px">
  <svg viewBox="0 0 24 24" fill="none" stroke="#fff" stroke-width="1.3"><path d="M5 17 15 7l3 3-10 10H5z"/><path d="M1 23h22"/></svg>
  <div><b>Create</b> Timelines, Maps, Family Trees</div>
</div>
<div class="abs feature" style="left:424px;top:587px;width:210px">
  <svg viewBox="0 0 24 24" fill="none" stroke="#fff" stroke-width="1.3"><rect x="2" y="1" width="18" height="22"/><rect x="5" y="4" width="12" height="14"/><circle cx="11" cy="9" r="2.5"/><path d="M7 17c1-4 7-4 8 0"/></svg>
  <div><b>Memorialize</b> Loved Ones</div>
</div>
<div class="abs feature" style="left:424px;top:633px;width:210px">
  <svg viewBox="0 0 24 24" fill="none" stroke="#fff" stroke-width="1.3"><path d="M8 10V6a4 4 0 0 1 8 0v4"/><rect x="5" y="10" width="14" height="13"/><path d="M12 15v3"/></svg>
  <div><b>Control</b> Your Privacy</div>
</div>
<div class="abs feature" style="left:664px;top:525px;width:190px">
  <svg viewBox="0 0 24 24" fill="none" stroke="#fff" stroke-width="1.3"><circle cx="18" cy="4" r="3"/><circle cx="5" cy="12" r="3"/><circle cx="18" cy="20" r="3"/><path d="M8 11 15 6M8 13l7 5"/></svg>
  <div><b>Share</b> Family Stories, History<br>and more</div>
</div>
<div class="abs feature" style="left:664px;top:585px;width:200px">
  <svg viewBox="0 0 24 24" fill="none" stroke="#fff" stroke-width="1.3"><circle cx="12" cy="12" r="11"/><path d="M16 4 8 20"/></svg>
  <div><b>No</b> Ads, No Like Buttons,<br><b>No</b> News Feeds</div>
</div>

<h2 class="abs blogs-title">Our latest Blogs</h2>
<div class="abs rule blogs-rule"></div>

<article class="abs post" style="left:71px">
  <div class="post-media logo-panel"><div class="img"></div><div class="tab"></div><div class="podcast-name">Quorvel Podcast</div></div>
  <div class="post-cat">PODCAST</div>
  <h3 class="post-title">Quorvel Podcast – Episode 5</h3>
  <div class="rule"></div>
  <p class="post-excerpt">As a part of a new series, Quorvel: Moments in Time, host Martin Calloway interviews special...</p>
</article>
<article class="abs post" style="left:350px">
  <div class="post-media photo-panel"><div class="img" role="img" aria-label="Podcast guest seated before a wall of framed theatre posters"></div><div class="tab"></div></div>
  <div class="post-cat">PODCAST</div>
  <h3 class="post-title">Quorvel Podcast – Episode 5</h3>
  <div class="rule"></div>
  <p class="post-excerpt">As a part of a new series, Quorvel: Moments in Time, host Martin Calloway interviews special...</p>
</article>
<article class="abs post" style="left:630px">
  <div class="post-media logo-panel"><div class="img"></div><div class="tab"></div><div class="podcast-name">Quorvel Podcast</div></div>
  <div class="post-cat">PODCAST</div>
  <h3 class="post-title">Quorvel Podcast – Episode 5</h3>
  <div class="rule"></div>
  <p class="post-excerpt">As a part of a new series, Quorvel: Moments in Time, host Martin Calloway interviews special...</p>
</article>

<footer class="abs site-footer">
  <div class="brand"><span class="brand-name">Quorvel</span></div>
  <nav class="footer-nav"><a>Privacy Policy</a><a>Terms &amp; Conditions</a><a>DTP</a><a>Feedback</a></nav>
  <div class="social"><a>Circlet</a><a>Chirper</a></div>
  <div class="footer-line"></div>
  <p class="copyright">Quorvel © 2017</p>
</footer>

</body>
</html>
```